Greyfield Ridge Medical Website to make connecting and communicating easier

To create a unique, user-friendly, professional website for patients and professionals to access education/ information, forms, appointments, contact details, and data about us, and for us to have the capacity to link to various cloud-based platforms.
To use the logo design and colour scheme we have just sourced.

WEBSITE to be eye catching, Inspiring and alluring
- efficient and logical
- professional and trustworthy appearance
- health focus "living health matters"
- user friendly
- ability to link with cloud-based software and video conferencing tools/ telehealth
- colours- black/ white teal and ?silver

PAGES:
page 1 - Our clinic and staff, services offered, contact us- address/ map / contact details- social media connections
page 2- patients and visitors - New patient forms to complete, news and patient informtion (educatinal)
page 3 - health professionals -referral forms, research and education
page 3- online appointments
page 4 - Quick links - partners, other services
page 5- privacy policy, disclaimer

HI, Could we please extend the deadline another 5 days, so sorry just struggling with my workload to be able to keep up and I am wanting to liaise more with the designer that I will choose. I am so happy with PixelHarbor and all the designers - thank you! Thank you so much!!

Target Market(s)

Patients - mostly over 60's so the website must be minimal clicks and simple to navigate
Professionals - for education and access forms

Industry/Entity Type

Health Care

Coding

Coded - Design and coding required

Number of Pages Required

5+ page

Font styles to use
Sans Serif
Script

Colors
33b8a4
86cfc6

Requirements
Must have
• WEBSITE to be eye catching, Inspiring and alluring
- efficient and logical
- user friendly

WEBSITE - professional and user friendly
- ability to link with cloud based software and videoconferencing/ telehealth
Nice to have
• clean and crisp presentation
happy for an innovative look
room to add more services and ability to link pages and resources
Should not have
• Please ensure the website is not:
clunky
difficult to navigate
common and cheap looking

```html
<!DOCTYPE html>
<html lang="en">
<head>
<meta charset="utf-8">
<title>Greyfield Ridge Medical – Patient Appointments</title>
<link rel="stylesheet" href="https://fonts.googleapis.com/css2?family=Montserrat:wght@400;500;600;700&family=Mulish:wght@400;600;700&display=swap">
<style>
:root{
  --teal:#33b8a4;
  --teal-dark:#1f9683;
  --teal-soft:#86cfc6;
  --ink:#1d3a34;
  --text:#333;
  --muted:#555;
  --panel:#f5f5f5;
  --line:#d9d9d9;
  --white:#fff;
}
*{box-sizing:border-box;margin:0;padding:0}
html,body{width:1200px;height:1200px;overflow:hidden;background:#fff}
body{font-family:'Mulish',sans-serif;color:var(--text)}
.page{position:absolute;left:332px;top:0;width:862px;height:1928px;transform:scale(.6211);transform-origin:0 0;background:#fff}
.abs{position:absolute}
.brand{display:flex;align-items:center;gap:6px;font-family:'Montserrat',sans-serif;font-weight:700;color:var(--teal);font-size:13px;line-height:1.1;white-space:nowrap}
.brand-dot{width:14px;height:14px;border-radius:50%;background:var(--teal);flex:none}

/* top bar */
.topbar{left:0;top:0;width:862px;height:77px;background:var(--panel)}
.topbar .brand{left:58px;top:31px}
.contact-chip{display:flex;align-items:center;gap:7px;font-size:9.5px;color:#333;top:32px;white-space:nowrap}
.contact-chip svg{width:14px;height:14px;flex:none}

/* nav */
.nav{left:0;top:77px;width:862px;height:54px;background:#fff}
.nav a{position:absolute;top:21px;font-size:11px;color:#222;text-decoration:none;letter-spacing:.1px;white-space:nowrap}
.nav a.active{color:var(--teal)}

/* hero */
.hero{left:0;top:131px;width:862px;height:202px;background:linear-gradient(100deg,#e7e9eb 0%,#d4d7da 40%,#b9bdc2 70%,#e2e5e8 100%)}
.hero-title{left:122px;top:64px;font-family:'Montserrat',sans-serif;font-weight:700;font-size:33px;line-height:1.05}
.hero-title span{display:block;color:var(--ink)}
.hero-title span.accent{color:var(--teal-dark)}

.section-title{position:absolute;left:0;width:862px;text-align:center;font-family:'Montserrat',sans-serif;font-weight:500;font-size:28px;color:var(--ink)}
.rule{position:absolute;height:3px;width:47px;background:var(--teal-dark);border-radius:2px}

.type-col h3{font-family:'Montserrat',sans-serif;font-weight:500;font-size:17px;color:#222;margin-bottom:9px}
.type-col p{font-size:10.5px;line-height:16px;color:#333;width:290px}

/* booking */
.booking{left:0;top:590px;width:862px;height:556px;background:var(--panel)}
.label{position:absolute;font-size:9px;color:#222;font-weight:600}
.field{position:absolute;height:32px;background:#fff;border:1px solid #e2e2e2;border-radius:6px;font-size:11px;color:#999;display:flex;align-items:center;justify-content:space-between;padding:0 10px}
.field.date{border:1.5px solid var(--teal)}
.textarea{position:absolute;left:64px;top:267px;width:427px;height:154px;background:#fff;border:1px solid #e2e2e2;border-radius:6px}
.btn{position:absolute;left:66px;top:439px;width:161px;height:30px;border-radius:15px;background:var(--teal);color:#fff;font-size:10px;font-weight:700;letter-spacing:.6px;display:flex;align-items:center;justify-content:center}

.calendar{position:absolute;left:523px;top:241px;width:274px;height:255px;background:#fff;border:1px solid #e2e2e2;border-radius:6px;box-shadow:0 2px 6px rgba(0,0,0,.06)}
.cal-head{position:absolute;top:11px;left:0;width:100%;text-align:center;font-size:12px;font-weight:600;color:#222}
.cal-arrow{position:absolute;top:11px;color:var(--teal);font-size:12px}
.cal-grid{position:absolute;left:5px;top:40px;display:grid;grid-template-columns:repeat(7,37.6px);grid-auto-rows:37.6px;font-size:9.5px;color:#222;text-align:center}
.cal-grid div{line-height:18px}
.cal-grid .dow{color:var(--teal);font-weight:600;line-height:18px}
.cal-grid .out{color:#ccc}

/* faq */
.faq-col{position:absolute;top:0;width:363px}
.faq-item{position:relative;border-bottom:1.5px solid var(--line)}
.faq-q{display:flex;align-items:center;gap:12px;font-family:'Montserrat',sans-serif;font-size:13px;color:#333;line-height:16px}
.faq-icon{width:32px;height:32px;border-radius:5px;background:var(--teal);flex:none;position:relative}
.faq-icon::before,.faq-icon::after{content:"";position:absolute;background:#fff;left:9px;top:15px;width:14px;height:1.5px}
.faq-icon.plus::after{left:15.25px;top:9px;width:1.5px;height:14px}
.faq-item.open{border-bottom:1.5px solid var(--teal-soft)}
.faq-item.open .faq-q{color:var(--teal-dark);font-weight:500}
.faq-answer{background:#f3f3f3;margin-top:6px;padding:16px 40px 10px 44px;font-size:10.5px;line-height:16px;color:#444}

/* footer */
.footer{left:0;top:1646px;width:862px;height:282px;background:var(--panel)}
.footer .brand{left:58px;top:62px;font-size:14px}
.f-head{position:absolute;font-size:11px;font-weight:600;color:#222;letter-spacing:.2px}
.f-list{position:absolute;list-style:none;font-size:9.5px;color:#222}
.f-list li{height:23.2px;white-space:nowrap}
.f-row{position:absolute;display:flex;gap:5px;font-size:9.5px;color:#222;line-height:16px;white-space:nowrap}
.f-row svg{width:13px;height:13px;margin-top:2px;flex:none}
.f-rule{position:absolute;left:58px;top:228px;width:747px;height:1px;background:#ccc}
.copyright{position:absolute;top:247px;left:0;width:862px;text-align:center;font-size:8px;color:#444}
.copyright a{color:var(--teal);text-decoration:underline}
</style>
</head>
<body>
<div class="page">

  <header class="abs topbar">
    <div class="abs brand"><span class="brand-dot"></span>Greyfield Ridge Medical</div>
    <div class="abs contact-chip" style="left:545px">
      <svg viewBox="0 0 16 16" fill="none" stroke="#33b8a4" stroke-width="1.3"><rect x="1.5" y="3.5" width="13" height="9" rx="1"/><path d="M1.5 4l6.5 5 6.5-5"/></svg>
      hello@greyfieldridge.com
    </div>
    <div class="abs contact-chip" style="left:708px">
      <svg viewBox="0 0 16 16" fill="none" stroke="#33b8a4" stroke-width="1.3"><path d="M4 1.8l2 3-1.3 1.4a8 8 0 0 0 5 5l1.4-1.3 3 2-1 2.2c-6 .4-11.6-5.2-11.2-11.2z"/></svg>
      (800) 555-0142
    </div>
  </header>

  <nav class="abs nav">
    <a class="active" style="left:58px">HOME</a>
    <a style="left:122px">ABOUT US</a>
    <a style="left:210px">OUR SERVICES</a>
    <a style="left:320px">PATIENTS &amp; VISITORS</a>
    <a style="left:465px">APPOINTMENTS</a>
    <a style="left:582px">NEWS &amp; INFORMATION</a>
    <a style="left:735px">CONTACT US</a>
  </nav>

  <section class="abs hero" role="img" aria-label="Photo of a doctor working at a computer showing medical scans in a bright clinic office">
    <h1 class="abs hero-title"><span>Patient</span><span class="accent">Appointments</span></h1>
  </section>

  <section class="abs" style="left:0;top:333px;width:862px;height:257px">
    <h2 class="section-title" style="top:44px">Appointment Types</h2>
    <div class="rule" style="left:292px;top:83px"></div>
    <div class="abs type-col" style="left:58px;top:103px">
      <h3>In-Office Visits</h3>
      <p>But I must explain to you how all this mistaken idea of denouncing pleasure and praising pain was born and I will give you a complete account of the system, and expound the actual teachings of the great explorer of the truth, the master-builder of human happiness.</p>
    </div>
    <div class="abs type-col" style="left:441px;top:103px">
      <h3 style="margin-left:3px">Virtual Visits</h3>
      <p>No one rejects, dislikes, or avoids pleasure itself, because it is pleasure, but because those who do not know how to pursue pleasure rationally encounter consequences that.</p>
    </div>
  </section>

  <section class="abs booking">
    <h2 class="section-title" style="top:54px">Make An Appointment</h2>
    <div class="rule" style="left:272px;top:92px"></div>

    <span class="label" style="left:67px;top:130px">Name*</span>
    <div class="field" style="left:67px;top:143px;width:215px"></div>
    <span class="label" style="left:297px;top:130px">Surname*</span>
    <div class="field" style="left:297px;top:143px;width:215px"></div>
    <span class="label" style="left:527px;top:130px">Phone*</span>
    <div class="field" style="left:527px;top:143px;width:215px"></div>

    <span class="label" style="left:64px;top:190px">Subject</span>
    <div class="field" style="left:64px;top:203px;width:215px">Select
      <svg width="10" height="10" viewBox="0 0 10 10" fill="none" stroke="#222" stroke-width="1.6"><path d="M2 3.5l3 3 3-3"/></svg></div>
    <span class="label" style="left:293px;top:190px">Doctor</span>
    <div class="field" style="left:293px;top:203px;width:215px">Select
      <svg width="10" height="10" viewBox="0 0 10 10" fill="none" stroke="#222" stroke-width="1.6"><path d="M2 3.5l3 3 3-3"/></svg></div>
    <span class="label" style="left:522px;top:190px">Date</span>
    <div class="field date" style="left:522px;top:203px;width:216px">mm/dd/yyyy
      <svg width="15" height="15" viewBox="0 0 16 16" fill="none" stroke="#33b8a4" stroke-width="1.3"><rect x="1.5" y="2.5" width="13" height="12" rx="1.5"/><path d="M1.5 6h13M5 1v3M11 1v3"/><rect x="4" y="8.5" width="2" height="2" fill="#33b8a4" stroke="none"/><rect x="7" y="8.5" width="2" height="2" fill="#33b8a4" stroke="none"/></svg></div>

    <span class="label" style="left:64px;top:254px">Message</span>
    <div class="textarea"></div>
    <div class="btn">Make An Appointment</div>

    <div class="calendar">
      <span class="cal-arrow" style="left:15px">&#8249;</span>
      <div class="cal-head">June 2020</div>
      <span class="cal-arrow" style="right:17px">&#8250;</span>
      <div class="cal-grid">
        <div class="dow">Mon</div><div class="dow">Tue</div><div class="dow">Wed</div><div class="dow">Thu</div><div class="dow">Fri</div><div class="dow">Sat</div><div class="dow">Sun</div>
        <div>1</div><div>2</div><div>3</div><div>4</div><div>5</div><div>6</div><div>7</div>
        <div>8</div><div>9</div><div>10</div><div>11</div><div>12</div><div>13</div><div>14</div>
        <div>15</div><div>16</div><div>17</div><div>18</div><div>19</div><div>20</div><div>21</div>
        <div>22</div><div>23</div><div>24</div><div>25</div><div>26</div><div>27</div><div>28</div>
        <div>29</div><div>30</div><div class="out">1</div><div class="out">2</div><div class="out">3</div><div class="out">4</div><div class="out">5</div>
      </div>
    </div>
  </section>

  <section class="abs" style="left:0;top:1146px;width:862px;height:500px">
    <h2 class="section-title" style="top:46px;left:14px">Frequently Asked Questions</h2>
    <div class="rule" style="left:247px;top:84px"></div>

    <div class="abs" style="left:0;top:129px;width:862px">
      <div class="faq-col" style="left:71px">
        <div class="faq-item" style="height:45px"><div class="faq-q"><span class="faq-icon plus"></span>How does it work?</div></div>
        <div class="faq-item open" style="margin-top:11px"><div class="faq-q"><span class="faq-icon"></span>Is my visit private and protected?</div>
          <div class="faq-answer">But I must explain to you how all this mistaken idea of denouncing pleasure and praising pain was born and I will give you a complete account of the system, and expound the actual teachings of the great explorer of the truth, the master-builder of human happiness. No.</div></div>
        <div class="faq-item" style="margin-top:21px;height:49px"><div class="faq-q"><span class="faq-icon plus"></span>Will my provider have access to my health records during my virtual visit?</div></div>
        <div style="margin-top:15px"><div class="faq-q"><span class="faq-icon plus"></span>Who can help me if I have technical issues with my virtual visit?</div></div>
      </div>
      <div class="faq-col" style="left:454px">
        <div class="faq-item" style="height:45px"><div class="faq-q"><span class="faq-icon plus"></span>How does it work?</div></div>
        <div class="faq-item open" style="margin-top:11px"><div class="faq-q"><span class="faq-icon"></span>Is my visit private and protected?</div>
          <div class="faq-answer">But I must explain to you how all this mistaken idea of denouncing pleasure and praising pain was born and I will give you a complete account of the system, and expound the actual teachings of the great explorer of the truth, the master-builder of human happiness. No.</div></div>
        <div class="faq-item" style="margin-top:21px;height:49px"><div class="faq-q"><span class="faq-icon plus"></span>Will my provider have access to my health records during my virtual visit?</div></div>
        <div style="margin-top:15px"><div class="faq-q"><span class="faq-icon plus"></span>Who can help me if I have technical issues with my virtual visit?</div></div>
      </div>
    </div>
  </section>

  <footer class="abs footer">
    <div class="abs brand"><span class="brand-dot"></span>Greyfield Ridge Medical</div>

    <span class="f-head" style="left:292px;top:41px">CONTACT</span>
    <div class="f-row" style="left:275px;top:72px">
      <svg viewBox="0 0 16 16" fill="none" stroke="#33b8a4" stroke-width="1.3"><path d="M8 15s5-5 5-9A5 5 0 0 0 3 6c0 4 5 9 5 9z"/><circle cx="8" cy="6" r="1.8"/></svg>
      <span>48 Ridgeway Ave.<br>Tempe, AZ 85281</span></div>
    <div class="f-row" style="left:275px;top:120px">
      <svg viewBox="0 0 16 16" fill="none" stroke="#33b8a4" stroke-width="1.3"><rect x="1.5" y="3.5" width="13" height="9" rx="1"/><path d="M1.5 4l6.5 5 6.5-5"/></svg>
      <span>contact@greyfieldridge.com</span></div>
    <div class="f-row" style="left:275px;top:152px">
      <svg viewBox="0 0 16 16" fill="none" stroke="#33b8a4" stroke-width="1.3"><path d="M4 1.8l2 3-1.3 1.4a8 8 0 0 0 5 5l1.4-1.3 3 2-1 2.2c-6 .4-11.6-5.2-11.2-11.2z"/></svg>
      <span>(345)555-0199</span></div>

    <span class="f-head" style="left:535px;top:41px">MENU</span>
    <ul class="f-list" style="left:538px;top:76px">
      <li>About Us</li><li>Our Services</li><li>Patients &amp; Visitors</li><li>Appointments</li><li>News &amp; Information</li><li>Contact Us</li>
    </ul>

    <span class="f-head" style="left:739px;top:42px">FOLLOW US</span>
    <ul class="f-list" style="left:739px;top:74px">
      <li>Linkvale</li><li>Chirpline</li><li>Snapgrove</li><li>Circlespace</li><li>Reelhaven</li>
    </ul>

    <div class="f-rule"></div>
    <p class="copyright">©2020 Greyfield Ridge Medical. All Rights Reserved. &nbsp;&nbsp; <a>Disclaimer</a> | <a>Privacy Policy</a></p>
  </footer>

</div>
</body>
</html>
```